Verdant Rooms Stationary Set

Verdant Rooms is a bespoke interior design firm set to provide services to VIP clients with elegance and minimalism is the main theme for our stationary set. We require a full stationary set covering A4 letterhead, A4 & A3 envelopes, business cards, USB's, CDs, email signature and any other item the designer sees fit. logo is already designed and finalized, and we require the designer to use it as is without modifying the logo.

Address to be used on letterhead / business cards ...etc shall be as follows:

Phone : +971 2 518 3076
P.O. Box : 318947
Address: Block C&D, Bldg. 27, Court 14, Abu Dhabi, United Arab Emirates
Website: www.verdantrooms.example

Target Market(s)

VIP Clients

Industry/Entity Type

Interior Design

Font styles to use
Other font styles liked:
• something to be unique

Colors

Designer to choose colors to be used in the design.

Requirements
Must have
• Elegant, minimalistic
Nice to have
• Simple yet elegant design having a sharp yet clean cut format
Should not have
• No additional colours, just colours that are used in the logo (silver, black or gold)

```html
<!DOCTYPE html>
<html lang="en">
<head>
<meta charset="utf-8">
<title>Verdant Rooms — Business Cards</title>
<link href="https://fonts.googleapis.com/css2?family=Cormorant+Garamond:wght@400;500&family=Great+Vibes&display=swap" rel="stylesheet">
<style>
  :root {
    --backdrop: #2b2b2d;
    --card-dark: #3a3a3d;
    --silver: #d9d9db;
    --gold-deep: #a9854a;
    --gold-light: #d8c28a;
    --gold-text: #c8ad72;
    --white: #ffffff;
  }
  * { margin: 0; padding: 0; box-sizing: border-box; }
  html, body { width: 1200px; height: 960px; overflow: hidden; }
  body {
    background: var(--backdrop);
    display: flex;
    flex-direction: column;
    align-items: center;
    justify-content: center;
    gap: 64px;
    font-family: "Cormorant Garamond", Georgia, serif;
  }
  .card {
    position: relative;
    width: 640px;
    height: 366px;
    overflow: hidden;
    box-shadow: 0 10px 30px rgba(0,0,0,0.45);
  }
  .card-back {
    background: var(--card-dark);
    display: flex;
    align-items: center;
    justify-content: center;
  }
  .brand-name {
    font-family: "Cormorant Garamond", Georgia, serif;
    font-weight: 500;
    letter-spacing: 0.12em;
    text-transform: uppercase;
  }
  .card-back .brand-name {
    color: var(--silver);
    font-size: 40px;
  }
  .card-front {
    background: linear-gradient(120deg, var(--gold-deep) 0%, var(--gold-light) 100%);
  }
  .card-front .sweep {
    position: absolute;
    inset: 0;
    width: 100%;
    height: 100%;
  }
  .card-front .brand-name {
    position: absolute;
    left: 400px;
    top: 120px;
    width: 220px;
    text-align: center;
    color: var(--gold-text);
    font-size: 30px;
    line-height: 1.15;
  }
  .contact {
    position: absolute;
    left: 42px;
    top: 118px;
    color: var(--white);
  }
  .person-name {
    font-family: "Great Vibes", cursive;
    font-size: 36px;
    line-height: 1;
  }
  .person-title {
    font-size: 19px;
    margin: 2px 0 0 18px;
  }
  .address {
    font-size: 16px;
    line-height: 1.3;
    margin: 22px 0 0 50px;
  }
  .lines {
    list-style: none;
    margin: 16px 0 0 50px;
    font-size: 16px;
    line-height: 1.35;
  }
  .lines li { display: flex; align-items: center; gap: 10px; }
  .lines svg { width: 13px; height: 13px; flex: none; }
</style>
</head>
<body>
  <section class="card card-back">
    <span class="brand-name">Verdant Rooms</span>
  </section>

  <section class="card card-front">
    <svg class="sweep" viewBox="0 0 640 366" aria-hidden="true">
      <path d="M350 0 C335 180 450 300 600 300 L640 300 L640 0 Z" fill="#ffffff"/>
      <path d="M338 0 C318 195 440 318 640 310" fill="none" stroke="#ffffff" stroke-width="1.2"/>
    </svg>
    <span class="brand-name">Verdant<br>Rooms</span>

    <div class="contact">
      <p class="person-name">Daniel Hayes</p>
      <p class="person-title">President</p>
      <p class="address">P.O. Box : 318947,<br>Block C&amp;D, Bldg. 27, Court 14<br>Abu Dhabi, United Arab Emirates</p>
      <ul class="lines">
        <li>
          <svg viewBox="0 0 16 16"><path d="M4 1 L6.5 4.5 L5 6.5 C6 8.5 7.5 10 9.5 11 L11.5 9.5 L15 12 L13 15 C7 15 1 9 1 3 Z" fill="#fff"/></svg>
          +971 2 518 3076
        </li>
        <li>
          <svg viewBox="0 0 16 16"><rect x="1" y="3" width="14" height="10" fill="#fff"/><path d="M1 3 L8 9 L15 3" fill="none" stroke="#b8975c" stroke-width="1.2"/></svg>
          info@verdantrooms.example
        </li>
        <li>
          <svg viewBox="0 0 16 16"><circle cx="8" cy="8" r="7" fill="#fff"/><path d="M1 8 H15 M8 1 C4 5 4 11 8 15 M8 1 C12 5 12 11 8 15" fill="none" stroke="#b8975c" stroke-width="1"/></svg>
          www.verdantrooms.example
        </li>
      </ul>
    </div>
  </section>
</body>
</html>
```